Simple Business Cards for Self-employed Coach

Simple business card with a design that includes the BHG logo.
Using either only the logo color or additional colors that match the logo.

Integral Coaches reach deeply into the past, gathering wisdom from East and West, while still staying current with the frontiers of new discovery in cognitive science, genetics, and other disciplines. see https://www.brightharborgroup.com/what-is-integral-coaching/

Target Market(s)

Coaching Clients in Tokyo /Asia; in business organizations, but also outside

Industry/Entity Type

Life Coaching

Contact Information for Business Card

Tomas Rendell
Certified Integral Coach

4-2-9 Hinokubo
Setagaya 154-0932
Tokyo, Japan

Phone: +81 70 4817 6092
E-Mail: tomas.rendell@quillpost.net

Font styles to use
Sans Serif

Colors
00a990

Requirements
Must have
• include uploaded logo
• color fitting with BHG logo color
Nice to have
• simple, elegant design
Should not have
• clutter

```html
<!DOCTYPE html>
<html lang="en">
<head>
<meta charset="utf-8">
<title>BHG Integral Coach – Business Cards</title>
<link rel="stylesheet" href="https://fonts.googleapis.com/css2?family=Open+Sans:wght@400;600;700&display=swap">
<style>
  :root {
    --teal: #047a70;
    --ink-grey: #7a7a7a;
    --rule: #e4e4e4;
    --paper: #ffffff;
    --backdrop: #ecebe8;
  }
  * { margin: 0; padding: 0; box-sizing: border-box; }
  html, body {
    width: 1200px; height: 1000px; overflow: hidden;
    background: var(--backdrop);
    font-family: "Open Sans", Arial, sans-serif;
  }
  .card {
    position: absolute;
    left: 266px;
    width: 666px;
    height: 397px;
    box-shadow: 0 2px 6px rgba(0,0,0,0.18);
  }
  .card--front { top: 74px; background: var(--paper); }
  .card--back { top: 534px; background: var(--teal); }

  .brand {
    position: absolute;
    display: flex;
    align-items: center;
    gap: 14px;
    font-weight: 700;
    letter-spacing: 0.18em;
  }
  .brand__square { display: block; }
  .card--front .brand {
    left: 56px; top: 160px;
    font-size: 48px; color: var(--teal);
  }
  .card--front .brand__square { width: 30px; height: 30px; background: var(--teal); }
  .card--back .brand {
    left: 0; right: 0; top: 160px;
    justify-content: center;
    font-size: 64px; color: var(--paper);
  }
  .card--back .brand__square { width: 38px; height: 38px; background: var(--paper); }

  .divider {
    position: absolute;
    left: 333px; top: 106px;
    width: 1px; height: 180px;
    background: var(--rule);
  }
  .contact {
    position: absolute;
    left: 372px; top: 104px;
    color: var(--ink-grey);
    font-size: 16px;
    line-height: 21px;
  }
  .contact__name {
    font-size: 20px; line-height: 24px;
    font-weight: 700; color: var(--teal);
    letter-spacing: 0.01em;
  }
  .contact__title { margin-bottom: 12px; }
  .contact__address { font-style: normal; margin-bottom: 12px; }
  .contact__line { display: flex; align-items: center; gap: 9px; line-height: 24px; }
  .contact__icon { width: 14px; height: 14px; fill: var(--teal); flex: none; }
</style>
</head>
<body>
  <section class="card card--front">
    <div class="brand"><span class="brand__square"></span>BHG</div>
    <div class="divider"></div>
    <div class="contact">
      <div class="contact__name">TOMAS RENDELL</div>
      <div class="contact__title">Certified Integral Coach</div>
      <address class="contact__address">4-2-9 Hinokubo<br>Setagaya 154-0932<br>Tokyo, Japan</address>
      <div class="contact__line">
        <svg class="contact__icon" viewBox="0 0 24 24" aria-hidden="true"><path d="M6.6 10.8a15.1 15.1 0 0 0 6.6 6.6l2.2-2.2c.3-.3.7-.4 1-.2 1.1.4 2.3.6 3.6.6.6 0 1 .4 1 1V20c0 .6-.4 1-1 1A17 17 0 0 1 3 4c0-.6.4-1 1-1h3.5c.6 0 1 .4 1 1 0 1.3.2 2.5.6 3.6.1.3 0 .7-.2 1z"/></svg>
        <span>+81 70 4817 6092</span>
      </div>
      <div class="contact__line">
        <svg class="contact__icon" viewBox="0 0 24 24" aria-hidden="true"><path d="M2 5h20v14H2z M2 5l10 7 10-7" fill="var(--teal)"/><path d="M3 6l9 6.3L21 6" fill="none" stroke="#fff" stroke-width="1.6"/></svg>
        <span>tomas.rendell@quillpost.net</span>
      </div>
    </div>
  </section>

  <section class="card card--back">
    <div class="brand"><span class="brand__square"></span>BHG</div>
  </section>
</body>
</html>
```